Graphic Design Assets for Brash Ward – Wellness with a Rock 'n' Roll Edge

Forget clinical blue, pastel gradients, and soft corporate stock photos. Brash Ward is a movement shattering the traditional, sterile look of mental health and wellness. We need a designer with a youthful, high-signal, rock 'n' roll design sensibility; someone who understands grit, physical presence, and bold editorial design. If your aesthetic is closer to a classic vinyl gatefold or a gritty street brand than a pharmacy brochure, we want you.

Project Overview
We have a finalized brand book and a clear creative direction. What we need now is a killer suite of graphic design assets to break up text-heavy layouts and bring our brand to life across three core touchpoints: a new website, a pitch/presentation deck, and a downloadable lead-gen asset (White Paper).

We are looking for the design assets first. If you have UI/UX or layout skills, you can handle the full implementation of the deck and document. If you are strictly a visual asset designer, you can deliver the components for our web developer to build with.

Scope of Work & Deliverables
We need a cohesive set of visual assets, including:

Web & UI Assets: Custom iconography, striking section dividers, bold typographic styling elements, and graphic textures to turn a text-heavy website into an immersive user experience.

Presentation Elements: Master slide backgrounds, data visualization graphics, and framing assets to transform a standard 10-page presentation deck.

Editorial Layout Assets: Headers, callout box designs, and spot graphics to make a downloadable White Paper look like a premium, tactical, independent magazine.

Design Sensibility & Brand Vibe
The Aesthetic: Utilitarian, gritty, tactile, and high-signal. Think bold typography, stark contrast, and raw authenticity. Think punk rock or liberation propaganda.

What to Avoid: Standard corporate tech design, clinical/medical visuals, soft "self-help" tropes, and generic minimalist vectors.

Target Audience: Young men, mentors, and partners who value real-world agency, movement, and zero fluff.

```html
<!DOCTYPE html>
<html lang="en">
<head>
<meta charset="utf-8">
<title>Brash Ward — Pitch Deck Master Slides</title>
<link href="https://fonts.googleapis.com/css2?family=League+Gothic&family=Courier+Prime:wght@700&display=swap" rel="stylesheet">
<style>
  :root {
    --red: #ff0000;
    --black: #000000;
    --white: #ffffff;
    --paper: #efefef;
    --display: "League Gothic", "Arial Narrow", sans-serif;
    --mono: "Courier Prime", "Courier New", monospace;
  }
  * { margin: 0; padding: 0; box-sizing: border-box; }
  html, body { width: 840px; height: 1200px; overflow: hidden; background: var(--paper); }
  .sheet { position: relative; width: 840px; height: 1200px; }

  .slide {
    position: absolute; width: 340px; height: 191px; overflow: hidden;
    box-shadow: 0 1px 6px rgba(0,0,0,0.08);
  }
  .col-left { left: 61px; }
  .col-right { left: 439px; }
  .row-1 { top: 50px; } .row-2 { top: 277px; } .row-3 { top: 504px; }
  .row-4 { top: 732px; } .row-5 { top: 959px; }

  .bg-black { background: var(--black); }
  .bg-white { background: var(--white); }
  .bg-red { background: var(--red); }

  .block { position: absolute; }
  .fill-red { background: var(--red); }
  .fill-black { background: var(--black); }
  .fill-white { background: var(--white); }

  .title {
    position: absolute; font-family: var(--display); font-weight: 400;
    font-size: 46px; line-height: 43px; text-transform: uppercase;
    white-space: nowrap; letter-spacing: 0;
  }
  .subtitle {
    position: absolute; font-family: var(--display); font-weight: 400;
    font-size: 27px; line-height: 26px; text-transform: uppercase; white-space: nowrap;
  }
  .t-white { color: var(--white); }
  .t-black { color: var(--black); }
  .t-red { color: var(--red); }

  .copy {
    position: absolute; font-family: var(--mono); font-weight: 700;
    font-size: 7px; line-height: 8.6px; white-space: nowrap;
  }
  .centered { left: 0; right: 0; text-align: center; }

  .brand-mark {
    position: absolute; left: 30px; top: 14px; display: flex; align-items: center; gap: 4px;
    font-family: var(--display); font-size: 12px; line-height: 12px; color: var(--red);
    text-transform: uppercase;
  }
  .brand-dot { width: 11px; height: 11px; border-radius: 50%; background: var(--red); }
  .slide-url {
    position: absolute; right: 19px; top: 163px; font-family: var(--mono); font-weight: 700;
    font-size: 4px; color: var(--white);
  }
  .slide-url span { color: var(--red); }
</style>
</head>
<body>
<main class="sheet">

  <!-- 01 Manifest -->
  <section class="slide col-left row-1 bg-black">
    <div class="brand-mark"><span class="brand-dot"></span>Brash Ward</div>
    <h1 class="title t-white" style="left:30px; top:58px;">The Manifest</h1>
    <p class="copy t-white" style="left:30px; top:113px;">A jarring, unmistakable entry point. Zero<br>generic intro fluff.</p>
    <p class="slide-url">www.<span>brashward</span>.com</p>
  </section>

  <!-- 02 Digital Cage -->
  <section class="slide col-right row-1 bg-white">
    <div class="block fill-red" style="left:0; top:0; width:183px; height:150px;"></div>
    <div class="block fill-black" style="left:20px; top:0; width:141px; height:191px;"></div>
    <h2 class="title t-white" style="left:33px; top:19px;">The<br>Digital<br>Cage</h2>
    <p class="subtitle t-red" style="left:33px; top:145px;">(The Problem)</p>
    <p class="copy t-black" style="left:203px; top:73px;">Confronting the reality of<br>a generation living life<br>through a screen<br>(channeling the core<br>thesis of Hale/Garrow).</p>
  </section>

  <!-- 03 Rebellion -->
  <section class="slide col-left row-2 bg-white">
    <div class="block fill-red" style="left:79px; top:0; width:182px; height:191px;"></div>
    <div class="block fill-black" style="left:17px; top:26px; width:306px; height:140px;"></div>
    <h2 class="title t-white centered" style="top:43px;">The Rebellion</h2>
    <p class="subtitle t-red centered" style="top:83px;">(The Solution / Mission)</p>
    <p class="copy t-white centered" style="top:118px;">The pivot. Introducing Brash Ward not as a "wellness<br>program," but as a tactical real-world movement.</p>
  </section>

  <!-- 04 Real-World Agency -->
  <section class="slide col-right row-2 bg-white">
    <div class="block fill-red" style="left:0; top:21px; width:212px; height:149px;"></div>
    <div class="block fill-black" style="left:212px; top:39px; width:128px; height:113px;"></div>
    <h2 class="title t-white" style="left:30px; top:39px;">Real-World<br>Agency</h2>
    <p class="subtitle t-black" style="left:30px; top:121px;">(Core Pillars)</p>
    <p class="copy t-white" style="left:227px; top:69px;">Breaking down the<br>3 to 4 fundamental<br>mechanics of how<br>the movement<br>builds presence<br>and connection.</p>
  </section>

  <!-- 05 Metrics -->
  <section class="slide col-left row-3 bg-black">
    <h2 class="title t-white" style="left:30px; top:48px;">High-Signal Metrics</h2>
    <p class="subtitle t-red" style="left:30px; top:89px;">(Market Opportunity / Data)</p>
    <p class="copy t-white" style="left:30px; top:123px;">Proving the massive scale of young men, mentors, and partners<br>looking for zero-fluff solutions.</p>
  </section>

  <!-- 06 Playbook -->
  <section class="slide col-right row-3 bg-black">
    <div class="block fill-red" style="left:0; top:0; width:340px; height:37px;"></div>
    <div class="block fill-white" style="left:20px; top:0; width:157px; height:191px;"></div>
    <h2 class="title t-black" style="left:33px; top:20px;">The<br>Playbook</h2>
    <p class="subtitle t-red" style="left:33px; top:104px;">(How It Works<br>/ Ecosystem)</p>
    <p class="copy t-white" style="left:203px; top:73px;">Confronting the reality of<br>a generation living life<br>through a screen<br>(channeling the core<br>thesis of Hale/Garrow).</p>
  </section>

  <!-- 07 Validation -->
  <section class="slide col-left row-4 bg-black">
    <div class="block fill-white" style="left:0; top:0; width:215px; height:158px;"></div>
    <h2 class="title t-black" style="left:30px; top:14px;">The<br>Validation</h2>
    <p class="subtitle t-red" style="left:30px; top:96px;">(Social Proof /<br>Cultural Resonance)</p>
    <p class="copy t-white" style="left:234px; top:111px;">Showcasing the rapid<br>cultural buy-in and<br>alignment with<br>high-signal thinkers.</p>
  </section>

  <!-- 08 Roadmap -->
  <section class="slide col-right row-4 bg-red">
    <div class="block fill-white" style="left:212px; top:39px; width:128px; height:113px;"></div>
    <div class="block fill-black" style="left:0; top:21px; width:212px; height:149px;"></div>
    <h2 class="title t-white" style="left:30px; top:26px;">The<br>Roadmap</h2>
    <p class="subtitle t-red" style="left:30px; top:109px;">(Milestones /<br>Launch Timeline)</p>
    <p class="copy t-black" style="left:227px; top:83px;">The strategic rollout.<br>What happens next as<br>Spring 2026 launches.</p>
  </section>

  <!-- 09 Unit Economics -->
  <section class="slide col-left row-5 bg-white">
    <h2 class="title t-black" style="left:30px; top:48px;">The Unit Economics</h2>
    <p class="subtitle t-red" style="left:30px; top:89px;">(The Model)</p>
    <p class="copy t-black" style="left:30px; top:123px;">The financial or operational feasibility structure behind<br>the movement.</p>
  </section>

  <!-- 10 Enlist Now -->
  <section class="slide col-right row-5 bg-red">
    <div class="block fill-black" style="left:79px; top:0; width:182px; height:191px;"></div>
    <div class="block fill-white" style="left:17px; top:27px; width:306px; height:138px;"></div>
    <h2 class="title t-black centered" style="top:43px;">Enlist Now</h2>
    <p class="subtitle t-red centered" style="top:83px;">(The Call to Action)</p>
    <p class="copy t-black centered" style="top:118px;">The final handshake. High-signal, uncompromising<br>instruction on how to jump in.</p>
  </section>

</main>
</body>
</html>
```